Varimel Sciences needs high end Label Design for a revolutionary new supplement

We at Varimel Sciences are looking for a brand new Label Design for a first of its kind product called Morivane. It is the first supplement on the market that treats grief and heartbreak. This product is unisex for both men and woman. We want the New Label to look high end and luxurious using the brand colors which are gold and burgundy. Please feel free to use other colors such as black, white, or gray to go along with it or any other colors if you feel would be a great fit! Varimel Sciences is like the Zephlon of the supplement world, coming out with new products that will challenge the way people treat different symptoms. To Recap:

1. Product Name: MORIVANE - the font will play a big roll
2. The Label will be placed on an all white bottle
3. Some parts of the label will be printed with foil to make parts of the label shiny and more attractive. Please keep this in mind when designing.
4. Must use our Logo. I will attach a file of our logo and of the emblem as well. Feel free to use the emblem separately if you have a great idea for it. Please let us know if you need the Logo in a different file type.
5. This all natural herbal supplement in pill form is the first to treat grief and support someone with a broken heart. The consumers purchasing this product will be going through a hard and emotional time. This is a serious product.
6. The manufacturer has included some basic instructions regarding the dye line and file types. Please do your best to meet these. If you cannot meet the guidelines please submit art work anyways. If your design is chosen we will just have the manufacturer replicate the design.

The final label should portray Morivane and Varimel Sciences as a luxurious brand and product which was made with cutting edge science leading the way with revolutionary ideas. We want customers to feel that the product is worth every penny, because it is. As soon as they receive the product and take one look at the label, I want them to think WOW I made the right choice buying this. I have attached some Label designs that we really liked for your review.

Please feel free to message me with any questions or if you need the Logo in a different file type. Thank you all.
Updates

Please send in more entries while we take a couple days to review, we are still looking for that one design we can work with. We are getting close, thank you all!

Target Market(s)

People going through grief and heartbreak.

Font styles to use
Sans Serif
Script
Other font styles liked:
• Any font that looks good, The font for the name MORIVANE is very important and will brand it. We hated the font used in the label we received in our first label draft (attached so you can see)

Requirements
Must have
• Must have the company Logo that says the company name
• Must have the colors Gold and Burgundy
• Must have some areas that will be the shiny foil when label is printed.
• Must say "Dietary Supplement" somewhere near the bottom along with "90 Capsules"
• I have attached a Label someone designed for us but were not really happy with. I did like the font the "Dietary supplement" and "90 Capsules" had and also where it was placed. We absolutely HATED the font used for Morivane.
• Must look at the label design we received from the manufacturer and take into consideration the room needed to write in the directions and all the symbols such as "made in america" and "QPA Facility" Don't worry about adding these in as they will put those in before printing but keep in mind they will be added to the Final Label along with the Supplement Facts.
Nice to have
• Would like to see other colors to go with gold and burgundy suck as black, white, or gray. I have attached some Label designs that I really liked for your reference.
Should not have
• Does not need to have any other legal language, that will be applied by the the manufacturer's graphics team.

```html
<!DOCTYPE html>
<html lang="en">
<head>
<meta charset="utf-8">
<title>Morivane Label</title>
<link rel="stylesheet" href="https://fonts.googleapis.com/css2?family=Archivo+Black&family=Arimo:wght@400;700&family=Lato:ital,wght@0,400;0,700;0,900;1,900&family=Cinzel:wght@500&display=swap">
<style>
  :root {
    --backdrop: #808184;
    --burgundy: #5c1019;
    --burgundy-deep: #3a080e;
    --gold: #d6a441;
    --gold-light: #e9c66a;
    --gold-dark: #8a5a1e;
    --paper: #ffffff;
    --ink: #111111;
  }
  * { margin: 0; padding: 0; box-sizing: border-box; }
  html, body { width: 1200px; height: 572px; overflow: hidden; background: var(--backdrop); }
  .label {
    position: absolute; left: 120px; top: 94px; width: 964px; height: 385px;
    background: linear-gradient(90deg, var(--burgundy) 0%, var(--burgundy-deep) 45%, var(--burgundy) 100%);
    box-shadow: 4px 6px 10px rgba(0,0,0,.35);
    overflow: hidden;
    font-family: "Lato", sans-serif;
  }
  .foil-band {
    position: absolute; left: 0; top: 0; width: 100%; height: 19px;
    background: linear-gradient(90deg, var(--gold-dark), var(--gold-light) 45%, var(--gold) 60%, var(--gold-dark));
  }
  .panel-shape { position: absolute; left: 0; top: 0; width: 964px; height: 385px; }

  .info { position: absolute; left: 22px; top: 38px; width: 240px; color: var(--gold); font-size: 7.4px; line-height: 1.25; }
  .info p { margin-bottom: 9px; }
  .info b { font-weight: 700; }
  .info .precautions { margin-top: 18px; text-transform: uppercase; }

  .badges { position: absolute; left: 22px; top: 221px; display: flex; gap: 10px; }
  .badge { width: 40px; text-align: center; color: var(--gold); font-size: 7.2px; }
  .badge-mark { width: 30px; height: 30px; margin: 0 auto 6px; border-radius: 50%; border: 2px solid var(--gold); background: rgba(214,164,65,.15); }

  .dates { position: absolute; left: 181px; top: 297px; color: var(--gold); font-size: 9px; line-height: 1.45; }

  .brand { position: absolute; left: 380px; top: 50px; width: 200px; text-align: center; color: var(--burgundy); font-family: "Cinzel", serif; font-weight: 500; }
  .brand-dot { width: 52px; height: 52px; margin: 0 auto 12px; border-radius: 50%; background: radial-gradient(circle at 40% 35%, var(--gold-light), var(--gold-dark)); }
  .brand-name { font-size: 26px; letter-spacing: 2px; line-height: 1; }
  .brand-sub { font-size: 19px; letter-spacing: 4px; line-height: 1.1; }

  .product-name {
    position: absolute; left: 330px; top: 181px; width: 320px; text-align: center;
    font-family: "Archivo Black", sans-serif; font-size: 54px; line-height: 1; color: var(--burgundy);
    -webkit-text-stroke: 1px var(--gold); text-shadow: 2px 2px 0 var(--gold-dark);
  }
  .product-type { position: absolute; left: 392px; top: 267px; width: 200px; text-align: center; font-weight: 900; font-style: italic; font-size: 16px; line-height: 1.25; color: var(--ink); }

  .count {
    position: absolute; left: 328px; top: 280px; width: 88px; height: 88px; border-radius: 50%;
    background: var(--burgundy); border: 4px solid var(--gold);
    color: var(--gold); text-align: center; font-weight: 900;
    display: flex; flex-direction: column; justify-content: center;
  }
  .count-num { font-size: 26px; line-height: 1; }
  .count-unit { font-size: 13px; }

  .facts { position: absolute; left: 690px; top: 40px; width: 252px; border: 2px solid var(--ink); padding: 3px 5px 2px; font-family: "Arimo", sans-serif; color: var(--ink); background: var(--paper); }
  .facts-title { font-family: "Archivo Black", sans-serif; font-size: 22px; line-height: 1.05; }
  .facts-serving { font-size: 10px; padding-bottom: 3px; border-bottom: 6px solid var(--ink); }
  .facts-head, .facts-row { display: flex; font-size: 9.6px; }
  .facts-head { font-weight: 700; padding: 2px 0; border-bottom: 3px solid var(--ink); }
  .facts-row { padding: 4px 0; border-bottom: 1px solid var(--ink); }
  .facts-row:last-of-type { border-bottom: 6px solid var(--ink); }
  .c-name { flex: 1; } .c-amt { width: 52px; } .c-dv { width: 20px; text-align: right; }
  .facts-note { font-size: 9.4px; padding-top: 2px; }
  .other { position: absolute; left: 692px; top: 216px; width: 262px; font-family: "Arimo", sans-serif; font-size: 9.2px; line-height: 1.3; color: var(--ink); }
  .other p + p { margin-top: 3px; }

  .distributor { position: absolute; left: 692px; top: 323px; color: var(--gold); font-weight: 700; font-size: 16px; line-height: 1.3; }
</style>
</head>
<body>
<main class="label">
  <div class="foil-band"></div>
  <svg class="panel-shape" viewBox="0 0 964 385" aria-hidden="true">
    <defs>
      <linearGradient id="foil" x1="0" x2="1" y1="0" y2="0">
        <stop offset="0" stop-color="#8a5a1e"/><stop offset=".5" stop-color="#e9c66a"/><stop offset="1" stop-color="#b07c2c"/>
      </linearGradient>
    </defs>
    <path d="M368 19 H964 V290 C840 300 720 318 560 345 C470 360 400 366 360 354 C330 300 300 230 312 146 C318 90 340 50 368 19 Z" fill="#ffffff"/>
    <path d="M368 19 C340 50 318 90 312 146 C300 230 330 300 360 354 C400 366 470 360 560 345 C720 318 840 300 964 290" fill="none" stroke="url(#foil)" stroke-width="6"/>
  </svg>

  <section class="info">
    <p><b>Direction:</b> Adult take 2 Capsules daily, as a dietary supplement. Or as directed by a health practitioner</p>
    <p><b>Benefits:</b> Promote fat burning, help to control the weight.</p>
    <p><b>Warnings:</b> If you are pregnant or breastfeeding, persons under the age of 18, consult a doctor before use. Do not use if you are hypersensitive to any of the formula ingredients.</p>
    <p><b>Storage Condition:</b> Keep container tightly sealed in a cool and dry place. Avoid heat and light.</p>
    <p class="precautions"><b>Precautions:</b><br>Do not use this product if safety seal is missing or broken keep out of reach of children.</p>
  </section>

  <div class="badges">
    <div class="badge"><div class="badge-mark"></div>Cruelty Free</div>
    <div class="badge"><div class="badge-mark"></div>Sugar Free</div>
    <div class="badge"><div class="badge-mark"></div>Dairy Free</div>
    <div class="badge"><div class="badge-mark"></div>Gluten Free</div>
    <div class="badge"><div class="badge-mark"></div>Non GMO</div>
  </div>

  <div class="dates">Manufacturing:<br>00 / 00 /00<br>Expiry date:<br>00 / 00 /00</div>

  <div class="brand">
    <div class="brand-dot"></div>
    <div class="brand-name">VARIMEL</div>
    <div class="brand-sub">SCIENCES</div>
  </div>

  <h1 class="product-name">MORIVANE</h1>
  <div class="product-type">DIETARY<br>SUPPLEMENT</div>

  <div class="count"><span class="count-num">90</span><span class="count-unit">Capsules</span></div>

  <section class="facts">
    <div class="facts-title">Supplement Facts</div>
    <div class="facts-serving">Serving Size 1 Capsule</div>
    <div class="facts-head"><span class="c-name">Amount Per Serving</span><span>% DV</span></div>
    <div class="facts-row"><span class="c-name">Milk Thistle Seed Extract<br>&nbsp;&nbsp;&nbsp;standardized to 80% silymarin<br>(140 mg)</span><span class="c-amt">175 mg</span><span class="c-dv">**</span></div>
    <div class="facts-row"><span class="c-name">Blessed Thistle (stem. leaf, Flower)</span><span class="c-amt">120 mg</span><span class="c-dv">**</span></div>
    <div class="facts-note">**Daily Value (DV) not established.</div>
  </section>

  <div class="other">
    <p>Other Ingredients: plant-derived capsule (hypromellose), Cellulose</p>
    <p>GLUTEN-FREE, SUGAR-FREE, NO PRESERVATIVES ADDED, NO ARTIFICIAL FLAVOR</p>
  </div>

  <div class="distributor">Distributed by:<br>Varimel Sciences, LLC</div>
</main>
</body>
</html>
```